Design a modern, classy & professional business card for an online real estate agency, specializing in medium-luxury properties in Thailand and later in Singapore and UK.

Possible design ideas so far: (not essential)

- curved corner(s) to the card, white on front & turquoise on back or visa versa.

- front of card - clear and simple, company name in metallic grey/monochrome, logo graphic & company name on front in spot UV or embossed/debossed effect.

- back of card - large, close-cropped, 'ghost' patterns of the C-shaped curves of logo, or company name repeated on back of card in spot UV.

Target Market(s)

- young to middle-aged professionals mainly (but ideally should design should suit all)

- UK, US,EU,AUS & ASIAN mainly (but ideally should design should suit all countries)

Industry/Entity Type

Real Estate

Requirements
Must have
• THEME:
- Luxurious & Modern
- Clean & striking
- Unique & creative

INFO:
- Logo & company name on front
- Contact details on back:

Tobias Lindqvar
Managing Director

www.velmoraestates.example
www.velmoraestates-uk.example

Tel: 084-273-6190
email: tobias@velmoraestates.example

(contact details can be displayed in any order as suites design.)

Nice to have
• - curved corner(s) to the card, white on front & turquoise on back or visa versa.

Should not have
• - No generic images of properties, palm trees/coconut trees etc.

- No other other bold colors, except for main turquoise, grey, metallic white & black theme.

- No obvious business card templates

```html
<!DOCTYPE html>
<html lang="en">
<head>
<meta charset="utf-8">
<title>Velmora Estates — Business Card</title>
<link rel="stylesheet" href="https://fonts.googleapis.com/css2?family=Cormorant+Garamond:wght@500&family=Cormorant+SC:wght@600&family=Open+Sans:wght@400;600&display=swap">
<style>
  :root {
    --turquoise: #4fc7c0;
    --turquoise-light: #63d2cb;
    --turquoise-dark: #3fb5ae;
    --grey: #8a8d8f;
    --grey-dark: #55595c;
    --white: #ffffff;
    --stage: #ecebe8;
  }
  * { margin: 0; padding: 0; box-sizing: border-box; }
  html, body { width: 1200px; height: 800px; overflow: hidden; }
  body { background: var(--stage); position: relative; font-family: "Open Sans", sans-serif; }

  .card { position: absolute; border-radius: 18px; overflow: hidden; box-shadow: 0 6px 20px rgba(0,0,0,.12); }

  /* Back */
  .card-back { left: 90px; top: 120px; width: 320px; height: 560px; background: var(--turquoise); }
  .back-pattern {
    position: absolute; inset: 0;
    background: linear-gradient(160deg, var(--turquoise-light), var(--turquoise) 55%, var(--turquoise-dark));
  }
  .back-brand {
    position: absolute; left: 58px; top: 46px;
    display: flex; flex-direction: column; align-items: center; gap: 12px;
  }
  .back-brand .mark { width: 26px; height: 26px; border: 2px solid var(--white); border-radius: 50%; }
  .back-brand .brand-name {
    writing-mode: vertical-rl;
    font-family: "Cormorant Garamond", serif; font-weight: 500;
    font-size: 34px; color: var(--white); letter-spacing: .5px;
  }

  /* Front */
  .card-front { left: 470px; top: 210px; width: 640px; height: 380px; background: var(--white); }
  .front-brand { position: absolute; left: 40px; top: 44px; display: flex; align-items: center; gap: 16px; }
  .front-brand .mark { width: 96px; height: 96px; background: var(--turquoise); flex: none; }
  .front-brand .brand-name {
    width: 150px;
    font-family: "Cormorant Garamond", serif; font-weight: 500;
    font-size: 40px; color: var(--grey); line-height: 1;
  }

  .holder { position: absolute; right: 40px; top: 58px; text-align: right; }
  .holder-name {
    font-family: "Cormorant SC", serif; font-weight: 600;
    font-size: 32px; color: var(--turquoise); letter-spacing: 1px; line-height: 1.1;
    white-space: nowrap;
  }
  .holder-title { font-size: 15px; font-weight: 600; color: var(--grey-dark); margin-top: 4px; }

  .contacts { position: absolute; left: 300px; top: 170px; list-style: none; }
  .contacts li {
    display: flex; align-items: center; gap: 10px;
    font-size: 15px; color: var(--grey-dark); line-height: 1; margin-bottom: 11px;
    white-space: nowrap;
  }
  .contacts svg { width: 16px; height: 16px; flex: none; }
</style>
</head>
<body>

<section class="card card-back" aria-label="Card back">
  <div class="back-pattern" role="img" aria-label="Faint tone-on-tone repeating ring pattern in turquoise"></div>
  <div class="back-brand">
    <span class="mark"></span>
    <span class="brand-name">Velmora Estates</span>
  </div>
</section>

<section class="card card-front" aria-label="Card front">
  <div class="front-brand">
    <span class="mark"></span>
    <span class="brand-name">Velmora Estates</span>
  </div>

  <div class="holder">
    <p class="holder-name">Tobias Lindqvar</p>
    <p class="holder-title">Managing Director</p>
  </div>

  <ul class="contacts">
    <li>
      <svg viewBox="0 0 16 16" aria-hidden="true"><circle cx="8" cy="8" r="8" fill="var(--turquoise)"/><path d="M5.2 4.2l1.4-.3.8 2-1 .7a5 5 0 0 0 2.9 2.9l.7-1 2 .8-.3 1.4c-3.7.3-6.8-2.8-6.5-6.5z" fill="#fff"/></svg>
      084-273-6190
    </li>
    <li>
      <svg viewBox="0 0 16 16" aria-hidden="true"><circle cx="8" cy="8" r="8" fill="var(--turquoise)"/><rect x="4" y="5.2" width="8" height="5.6" rx=".6" fill="#fff"/><path d="M4.3 5.6L8 8.4l3.7-2.8" stroke="var(--turquoise)" stroke-width=".9" fill="none"/></svg>
      tobias@velmoraestates.example
    </li>
    <li>
      <svg viewBox="0 0 16 16" aria-hidden="true"><circle cx="8" cy="8" r="8" fill="var(--turquoise)"/><g stroke="#fff" stroke-width=".9" fill="none"><circle cx="8" cy="8" r="4.2"/><ellipse cx="8" cy="8" rx="1.8" ry="4.2"/><path d="M3.8 8h8.4"/></g></svg>
      www.velmoraestates.example
    </li>
    <li>
      <svg viewBox="0 0 16 16" aria-hidden="true"><circle cx="8" cy="8" r="8" fill="var(--turquoise)"/><g stroke="#fff" stroke-width=".9" fill="none"><circle cx="8" cy="8" r="4.2"/><ellipse cx="8" cy="8" rx="1.8" ry="4.2"/><path d="M3.8 8h8.4"/></g></svg>
      www.velmoraestates-uk.example
    </li>
  </ul>
</section>

</body>
</html>
```